Business card design for industrial spray painting - startup business

Design the layout of our new business card using the logo we have provided.

We want the card to be matt black in colour.

We only want our logo and slogan on the face side.

Because the card is black we would like the slogan WE COAT EVERYTHING! to be in white.

We want our information on the rear side.

I would like my name in blue matching the blue in the logo.

The remainder of the information should be in grey to match the grey in the logo.

The overall finish should look minimal, clean and slick.

Our business is industrlal and of a masculine nature.

Target Market(s)

industrial and mining companies

Contact Information for Business Card

(front of card – matt black)
insert logo here:
insert this tag line: WE COAT EVERYTHING!

--------------------------------------------------------------------------------------------------------------

(back of card – matt black)
Dorian Kestle
Paint and Coatings Specialist
47 Millbrook Avenue, Bayswater WA 6053
M: +61 437 281 914
T: +61 8 555 7318
E: dorian@coatlynx.co
W: www.coatlynx.co

Font styles to use
Sans Serif

Colors
000000
0455a3

Requirements
Must have
• clean, slick minimalist look. Masculine as we deal mostly with industrial spray painting

```html
<!DOCTYPE html>
<html lang="en">
<head>
<meta charset="utf-8">
<title>Coatlynx Business Card</title>
<link rel="stylesheet" href="https://fonts.googleapis.com/css2?family=Michroma&family=Arimo:wght@400&display=swap">
<style>
  :root {
    --backdrop: #2b2622;
    --card-black: #000000;
    --brand-blue: #0455a3;
    --accent-blue: #1f7fd6;
    --brand-grey: #9a9a9a;
    --light-grey: #c4c4c4;
  }
  * { margin: 0; padding: 0; box-sizing: border-box; }
  html, body {
    width: 1200px;
    height: 913px;
    overflow: hidden;
    background: var(--backdrop);
  }
  .canvas {
    position: relative;
    width: 1200px;
    height: 913px;
  }
  .card {
    position: absolute;
    width: 560px;
    height: 320px;
    background: var(--card-black);
    box-shadow: 0 18px 40px rgba(0, 0, 0, 0.55);
    overflow: hidden;
  }
  .card--front { left: 70px; top: 110px; }
  .card--back  { left: 570px; top: 480px; }

  .brand {
    display: flex;
    align-items: center;
    gap: 12px;
    font-family: "Michroma", sans-serif;
    color: var(--accent-blue);
    letter-spacing: 2px;
    white-space: nowrap;
  }
  .brand__mark {
    width: 20px;
    height: 20px;
    background: var(--accent-blue);
    flex: none;
  }

  .card--front .brand {
    position: absolute;
    left: 0; right: 0;
    top: 120px;
    justify-content: center;
    font-size: 34px;
  }
  .card--front .brand__mark { width: 28px; height: 28px; }
  .tagline {
    position: absolute;
    left: 0; right: 0;
    top: 205px;
    text-align: center;
    font-family: "Michroma", sans-serif;
    font-size: 14px;
    letter-spacing: 3px;
    color: var(--light-grey);
    white-space: nowrap;
  }

  .card--back .brand {
    position: absolute;
    left: 38px;
    top: 92px;
    font-size: 22px;
  }
  .divider {
    position: absolute;
    left: 0;
    top: 158px;
    width: 300px;
    height: 1.5px;
    background: var(--accent-blue);
  }
  .holder {
    position: absolute;
    left: 318px;
    top: 134px;
    white-space: nowrap;
  }
  .holder__name {
    font-family: "Michroma", sans-serif;
    font-size: 15px;
    letter-spacing: 1px;
    color: var(--accent-blue);
    text-transform: uppercase;
  }
  .holder__role {
    margin-top: 6px;
    font-family: "Arimo", sans-serif;
    font-size: 12.5px;
    color: var(--light-grey);
  }
  .address {
    position: absolute;
    left: 318px;
    top: 208px;
    display: flex;
    gap: 10px;
    font-family: "Arimo", sans-serif;
    font-size: 12px;
    line-height: 1.45;
    color: var(--brand-grey);
    white-space: nowrap;
  }
  .contacts {
    position: absolute;
    left: 70px;
    top: 190px;
    list-style: none;
    font-family: "Arimo", sans-serif;
    font-size: 12.5px;
    color: var(--brand-grey);
  }
  .contacts li {
    display: flex;
    align-items: center;
    gap: 12px;
    height: 24px;
    white-space: nowrap;
  }
  .icon { width: 16px; height: 16px; flex: none; }
</style>
</head>
<body>
<main class="canvas">

  <section class="card card--front" aria-label="Card front">
    <div class="brand"><span class="brand__mark"></span><span class="brand__name">COATLYNX</span></div>
    <p class="tagline">WE COAT EVERYTHING!</p>
  </section>

  <section class="card card--back" aria-label="Card back">
    <div class="brand"><span class="brand__mark"></span><span class="brand__name">COATLYNX</span></div>
    <div class="divider"></div>

    <div class="holder">
      <p class="holder__name">Dorian Kestle</p>
      <p class="holder__role">Paint and Coatings Specialist</p>
    </div>

    <div class="address">
      <svg class="icon" viewBox="0 0 16 16" aria-hidden="true">
        <path d="M8 1a5 5 0 0 0-5 5c0 3.8 5 9 5 9s5-5.2 5-9a5 5 0 0 0-5-5zm0 7a2 2 0 1 1 0-4 2 2 0 0 1 0 4z" fill="#1f7fd6"/>
      </svg>
      <p>47 Millbrook Avenue,<br>Redcliffe WA 6104</p>
    </div>

    <ul class="contacts">
      <li>
        <svg class="icon" viewBox="0 0 16 16" aria-hidden="true"><rect x="4" y="1" width="8" height="14" rx="1.5" fill="none" stroke="#1f7fd6" stroke-width="1.3"/></svg>
        <span>+61 437 281 914</span>
      </li>
      <li>
        <svg class="icon" viewBox="0 0 16 16" aria-hidden="true"><path d="M4 1.5l2.5 3-1.5 1.8c.8 1.7 2 2.9 3.7 3.7L10.5 8.5l3 2.5-1.5 2.5C7 13.5 2.5 9 2.5 4z" fill="#1f7fd6"/></svg>
        <span>+61 8 555 7318</span>
      </li>
      <li>
        <svg class="icon" viewBox="0 0 16 16" aria-hidden="true"><rect x="1.5" y="3.5" width="13" height="9" fill="#1f7fd6"/><path d="M1.5 3.5L8 9l6.5-5.5" fill="none" stroke="#000" stroke-width="1"/></svg>
        <span>dorian@coatlynx.co</span>
      </li>
      <li>
        <svg class="icon" viewBox="0 0 16 16" aria-hidden="true"><g fill="none" stroke="#1f7fd6" stroke-width="1.2"><circle cx="8" cy="8" r="6.5"/><ellipse cx="8" cy="8" rx="3" ry="6.5"/><path d="M1.5 8h13M2.5 5h11M2.5 11h11"/></g></svg>
        <span>www.coatlynx.co</span>
      </li>
    </ul>
  </section>

</main>
</body>
</html>
```